Private Optometric Practice Needs new Presentation Folders/Stationary

We recently moved our office and are looking to refresh our presentation folders and stationary. I tend to prefer simple, clean designs. We are a full scope optometric practice provide high quality eyewear, custom contact lenses, along with emergency care and treatment for dry eyes. We communicate with a lot of other doctors and want to exude professionalism. I have attached 2 versions of our logo.

Target Market(s)

Familys

Industry/Entity Type

Eyecare

Font styles to use
Sans Serif

Colors
0054AA
0677BA
7BADD7
CADEEF
E8F1F8

Requirements
Nice to have
• Bifold, areas to put information about practice, welcome letter

```html
<!DOCTYPE html>
<html lang="en">
<head>
<meta charset="utf-8">
<title>Brightfield Vision — Business Card</title>
<link href="https://fonts.googleapis.com/css2?family=Montserrat:wght@600&family=Roboto:wght@300;400&display=swap" rel="stylesheet">
<style>
  :root {
    --backdrop: #1d1e21;
    --card-white: #f4f5f6;
    --wave-grey: #5c5d61;
    --wave-grey-dark: #46474b;
    --accent-blue: #5cc6ea;
    --text-grey: #6d6e72;
    --back-top: #56575b;
    --back-bottom: #333438;
    --back-text: #e6e7e9;
  }
  * { margin: 0; padding: 0; box-sizing: border-box; }
  html, body { width: 1200px; height: 900px; overflow: hidden; }
  body {
    background: var(--backdrop);
    font-family: "Roboto", Arial, sans-serif;
    position: relative;
  }
  .card {
    position: absolute;
    left: 267px;
    width: 665px;
    height: 380px;
    border-radius: 22px;
    overflow: hidden;
  }
  .card--front { top: 50px; background: var(--card-white); }
  .card--back {
    top: 470px;
    background: linear-gradient(160deg, var(--back-top), var(--back-bottom));
    display: flex; align-items: center; justify-content: center;
  }
  .card__wave { position: absolute; inset: 0; width: 100%; height: 100%; }
  .holder { position: absolute; left: 58px; top: 38px; }
  .holder__name {
    font-family: "Montserrat", Arial, sans-serif;
    font-weight: 600; font-size: 19px; letter-spacing: 0.5px;
    color: var(--accent-blue); text-transform: uppercase;
  }
  .holder__title { font-size: 16px; color: var(--text-grey); margin-top: 3px; }
  .contact {
    position: absolute; left: 58px; top: 112px;
    font-size: 16px; color: var(--text-grey); line-height: 1.35;
  }
  .contact__address { margin-bottom: 6px; }
  .contact__row { display: flex; align-items: center; gap: 8px; }
  .contact__icon { width: 15px; height: 15px; fill: none; stroke: var(--accent-blue); stroke-width: 1.6; }
  .contact__icon--solid { fill: var(--accent-blue); stroke: none; }
  .brand {
    position: absolute; right: 45px; top: 232px;
    display: flex; align-items: center; gap: 12px;
    white-space: nowrap;
  }
  .brand__mark { width: 26px; height: 26px; border-radius: 50%; background: var(--accent-blue); flex: none; }
  .brand__name {
    font-family: "Roboto", Arial, sans-serif; font-weight: 300;
    font-size: 22px; letter-spacing: 3px; color: var(--text-grey);
    text-transform: uppercase;
  }
  .card--back .brand { position: static; gap: 16px; }
  .card--back .brand__mark { width: 38px; height: 38px; }
  .card--back .brand__name { color: var(--back-text); font-size: 36px; letter-spacing: 6px; }
</style>
</head>
<body>
  <section class="card card--front">
    <svg class="card__wave" viewBox="0 0 665 380" preserveAspectRatio="none" aria-hidden="true">
      <defs>
        <linearGradient id="waveGrey" x1="0" y1="0" x2="1" y2="1">
          <stop offset="0" stop-color="var(--wave-grey)"/>
          <stop offset="1" stop-color="var(--wave-grey-dark)"/>
        </linearGradient>
      </defs>
      <path d="M0,272 C150,266 250,338 400,346 C520,352 600,322 665,282 L665,380 L0,380 Z" fill="var(--accent-blue)"/>
      <path d="M0,274 C150,270 250,348 400,356 C520,362 600,338 665,300 L665,380 L0,380 Z" fill="url(#waveGrey)"/>
    </svg>

    <div class="holder">
      <p class="holder__name">Daniel Whitford, O.D.</p>
      <p class="holder__title">Founder &amp; CEO</p>
    </div>

    <div class="contact">
      <p class="contact__address">1420 Lakeview Pkwy. Suite B<br>Fairmont, MI 48210</p>
      <p class="contact__row">
        <svg class="contact__icon contact__icon--solid" viewBox="0 0 16 16" aria-hidden="true"><path d="M4 1 L6.5 1 L7.5 4.5 L5.8 5.8 C6.6 7.6 8.4 9.4 10.2 10.2 L11.5 8.5 L15 9.5 L15 12 C15 13.6 13.6 15 12 15 C6 15 1 10 1 4 C1 2.4 2.4 1 4 1 Z"/></svg>
        (555) 318-4720
      </p>
      <p class="contact__row">
        <svg class="contact__icon" viewBox="0 0 16 16" aria-hidden="true"><rect x="1.5" y="3.5" width="13" height="9" rx="1"/><path d="M1.5 4 L8 9 L14.5 4"/></svg>
        hello@brightfieldvision.com
      </p>
      <p class="contact__row">
        <svg class="contact__icon" viewBox="0 0 16 16" aria-hidden="true"><circle cx="8" cy="8" r="6.5"/><ellipse cx="8" cy="8" rx="3" ry="6.5"/><path d="M1.5 8 H14.5"/></svg>
        www.brightfieldvision.com
      </p>
    </div>

    <div class="brand">
      <span class="brand__mark" aria-hidden="true"></span>
      <span class="brand__name">Brightfield Vision</span>
    </div>
  </section>

  <section class="card card--back">
    <div class="brand">
      <span class="brand__mark" aria-hidden="true"></span>
      <span class="brand__name">Brightfield Vision</span>
    </div>
  </section>
</body>
</html>
```